New Slide Master Template for PPT

I need a new Slide Master / Template for PPT presentations. Our company does Cloud Management / Network Management systems that are used to manage devices connected to the internet. Those devices can be things like Wireless Access Points, DSL modems, Cable modems, Gateways, Routers, Switches, and the equipment that is in the internet such as Brevok, Talsome, or Ormavin-Dusk equipment.
What our management system does is connect/communicate with all these different devices to be able to get information from the devices such as throughput performance, wireless coverage, failures conditions, firmware versions, and any other information which is used to manage, control, or troubleshoot those devices for the equipment companies or internet service providers who have provided them to their end customers for internet service.
The new Slide Master / Template for PowerPoint needs to do to the following;
1. be fresh and current in design
2. have a nice looking font that works for both print and presentation on small screens (laptops) as well as big screen (large group presentations)
3. not consume too many MegaBytes when saved as a file. Many email servers have limits on the size of files which can be transferred as an attachment. Most are either 5 or 10 MB limits. I do not want to have to zip the file to get it under such size restrictions.
4. the colors in the "Quorvian" logo are the company colors (the orange and blue), those should be incorporated in some form in the Slide Master / Template.
5. the final design should communicate professionalism with a modern look and feel.
6. once done the attached (old version of presentation) should be transferred over using the new Slide Master / Template and new fonts.
NOTE: I am not seeing how to attach my current PPT file to this project. Please email me at tobias@fernpathsystems.example and I will send you the current presentation which needs to be updated as described above.
Updates
Target Market(s)
Networking equipment manufacturers like Brevok, Pylorn, Ormavin-Dusk, VoxTe, etc.
Industry/Entity Type
Internet
Look and feel
Each slider illustrates characteristics of the customer's brand and the style your logo design should communicate.

```html
<!DOCTYPE html>
<html lang="en">
<head>
<meta charset="utf-8">
<title>Software Process and Methodology</title>
<link href="https://fonts.googleapis.com/css2?family=Merriweather:ital,wght@0,400;0,700;1,400&family=Open+Sans:wght@400;600;700&display=swap" rel="stylesheet">
<style>
  :root {
    --brand-blue: #1f6bb5;
    --box-blue: #2c80d8;
    --box-blue-dark: #1c63b3;
    --gold: #c99a2c;
    --gold-dark: #a87d1c;
    --slate: #575757;
    --slate-dark: #3f3f3f;
    --panel: #6f6f6f;
    --panel-item: #8b8b8b;
    --rule: #b9b9b9;
    --ink: #1a1a1a;
    --muted: #444;
  }
  * { margin: 0; padding: 0; box-sizing: border-box; }
  html, body { width: 1200px; height: 675px; overflow: hidden; background: #fff; }
  .slide {
    position: relative; width: 1200px; height: 675px; overflow: hidden;
    font-family: "Open Sans", Arial, sans-serif; color: var(--ink);
  }
  .backdrop {
    position: absolute; inset: 0;
    background: radial-gradient(ellipse at 60% 40%, #ffffff 0%, #f4f4f4 60%, #ececec 100%);
  }
  .diagram { position: absolute; inset: 0; }
  .title {
    position: absolute; left: 67px; top: 36px;
    font-family: "Merriweather", Georgia, serif; font-weight: 400;
    font-size: 35px; color: var(--brand-blue); letter-spacing: 0.2px;
  }
  .subtitle {
    position: absolute; left: 67px; top: 93px;
    font-family: "Merriweather", Georgia, serif; font-size: 24px; color: var(--ink);
  }
  .brand {
    position: absolute; left: 960px; top: 48px;
    display: flex; align-items: center; gap: 10px;
    font-family: "Open Sans", Arial, sans-serif; font-weight: 700;
    font-size: 34px; color: var(--brand-blue);
  }
  .brand-dot { width: 26px; height: 26px; border-radius: 50%; background: var(--gold); }
  .phase {
    position: absolute; top: 144px; width: 260px; text-align: center;
    font-family: "Merriweather", Georgia, serif; font-style: italic;
    font-size: 21px; color: var(--ink);
  }
  .box {
    position: absolute; display: flex; align-items: center; justify-content: center;
    text-align: center; color: #fff; font-weight: 700; font-size: 11.5px; line-height: 1.25;
    border-radius: 4px; padding: 0 4px;
  }
  .step { top: 305px; height: 58px; background: linear-gradient(#d4a63a, var(--gold-dark)); box-shadow: 0 2px 3px rgba(0,0,0,.25); }
  .output { top: 198px; height: 57px; background: linear-gradient(var(--box-blue), var(--box-blue-dark)); box-shadow: 0 2px 3px rgba(0,0,0,.25); }
  .activity {
    top: 430px; height: 67px; background: linear-gradient(#616161, var(--slate-dark));
    font-size: 13px; box-shadow: 0 2px 4px rgba(0,0,0,.3);
  }
  .process-panel {
    position: absolute; left: 527px; top: 427px; width: 248px; height: 193px;
    background: linear-gradient(#7a7a7a, #606060); border-radius: 6px;
    box-shadow: 0 2px 5px rgba(0,0,0,.3);
  }
  .process-item {
    position: absolute; left: 10px; width: 228px; height: 26px;
    background: linear-gradient(#939393, #7c7c7c); border: 1px solid #a5a5a5; border-radius: 3px;
    display: flex; align-items: center; justify-content: center;
    color: #fff; font-size: 10.5px;
  }
  .footer {
    position: absolute; left: 67px; top: 637px; font-size: 11.5px; color: var(--muted);
  }
  .page-number { position: absolute; left: 1142px; top: 636px; font-size: 12px; color: var(--muted); }
</style>
</head>
<body>
<div class="slide">
  <div class="backdrop" role="img" aria-label="Faint network of connected nodes across a light grey background"></div>

  <svg class="diagram" width="1200" height="675" viewBox="0 0 1200 675" aria-hidden="true">
    <defs>
      <linearGradient id="band" x1="0" y1="0" x2="0" y2="1">
        <stop offset="0" stop-color="#e4e4e4"/>
        <stop offset="0.5" stop-color="#d2d2d2"/>
        <stop offset="1" stop-color="#e6e6e6"/>
      </linearGradient>
      <marker id="head" viewBox="0 0 10 10" refX="5" refY="5" markerWidth="4" markerHeight="4" orient="auto-start-reverse">
        <path d="M0 0 L10 5 L0 10 Z" fill="var(--gold)"/>
      </marker>
    </defs>
    <line x1="67" y1="87" x2="935" y2="87" stroke="var(--rule)" stroke-width="1.5"/>
    <path d="M0 255 H1067 V203 L1190 320 L1067 437 V385 H0 Z" fill="url(#band)"/>
    <line x1="500" y1="118" x2="500" y2="622" stroke="var(--gold)" stroke-width="3" stroke-dasharray="2 6" stroke-linecap="round"/>
    <line x1="783" y1="118" x2="783" y2="622" stroke="var(--gold)" stroke-width="3" stroke-dasharray="2 6" stroke-linecap="round"/>
    <g stroke="var(--gold)" stroke-width="4">
      <line x1="329" y1="305" x2="329" y2="262" marker-end="url(#head)"/>
      <line x1="436" y1="305" x2="436" y2="262" marker-end="url(#head)"/>
      <line x1="868" y1="305" x2="868" y2="262" marker-end="url(#head)"/>
      <line x1="960" y1="305" x2="960" y2="262" marker-end="url(#head)"/>
      <line x1="645" y1="427" x2="645" y2="370" marker-end="url(#head)"/>
      <line x1="113" y1="370" x2="113" y2="423" marker-start="url(#head)" marker-end="url(#head)"/>
      <line x1="436" y1="370" x2="436" y2="423" marker-start="url(#head)" marker-end="url(#head)"/>
      <line x1="911" y1="370" x2="911" y2="423" marker-start="url(#head)" marker-end="url(#head)"/>
      <line x1="1083" y1="370" x2="1083" y2="423" marker-start="url(#head)" marker-end="url(#head)"/>
    </g>
  </svg>

  <h1 class="title">Software Process and Methodology</h1>
  <h2 class="subtitle">Project Life Cycle</h2>
  <div class="brand"><span class="brand-dot"></span>Quorvian</div>

  <div class="phase" style="left:145px">Project Plan</div>
  <div class="phase" style="left:508px">Project Execution</div>
  <div class="phase" style="left:863px">Project Summary</div>

  <div class="box output" style="left:280px;width:98px">Statement of Work</div>
  <div class="box output" style="left:387px;width:98px">Milestone based Schedule</div>
  <div class="box output" style="left:835px;width:66px">Bug Analysis Report</div>
  <div class="box output" style="left:913px;width:94px">Project Data</div>

  <div class="box step" style="left:63px;width:97px">Customer Engagement</div>
  <div class="box step" style="left:172px;width:97px">Project Investigation</div>
  <div class="box step" style="left:280px;width:98px">Project Quotation</div>
  <div class="box step" style="left:387px;width:98px">Project Plan</div>
  <div class="box step" style="left:517px;width:257px">Software Development Process</div>
  <div class="box step" style="left:835px;width:152px">Project Summary</div>
  <div class="box step" style="left:1015px;width:135px">Quality Training</div>

  <div class="box activity" style="left:57px;width:112px">On Site Customer Visit</div>
  <div class="box activity" style="left:382px;width:108px">Project Plan Review</div>
  <div class="box activity" style="left:857px;width:110px">Project Summary Meeting</div>
  <div class="box activity" style="left:1025px;width:120px">QA Training Meeting</div>

  <div class="process-panel">
    <div class="process-item" style="top:10px">Schedule Maintenance</div>
    <div class="process-item" style="top:46px">Requirement Management</div>
    <div class="process-item" style="top:81px">Risk Management</div>
    <div class="process-item" style="top:118px">Customer Relationship Management</div>
    <div class="process-item" style="top:153px">QA Management</div>
  </div>

  <div class="footer">Quorvian Technologies Corporation &nbsp;|&nbsp; 2013 © Confidential All Rights Reserved</div>
  <div class="page-number">11</div>
</div>
</body>
</html>
```